seeking a modern Business Card design for Roof Plumbering Business

hallowell roof plumbing is a local metal re-roof and new construction specialist. We are seeking a modern business card to assist with networking within the industry. Our services are predominantly the installation of metal roofs on new houses, however we also do re-roofs when an existing roof needs replacing. We service both residential and commercial properties. Please include the below details on the card:
Name: Owen Hallowell
Phone: 0417 382 965
Email: owenhallowellroofing@maildrop-example.com

Residential & Commercial
Re-roof & New Construction
Fully Insured

I have uploaded our business logo, which we think would suit a black background. Please use all lower case for business name.
Cheers
Updates

Hey Guys, As requested I've uploaded a Pdf version of my logo. Hopefully this help. Thanks

Industry/Entity Type

Business

Contact Information for Business Card

Name: Owen Hallowell
Phone: 0417 382 965

Residential & Commercial
Fully Insured

Font styles to use
Serif
Sans Serif

Requirements
Must have
• Name must be all lower case "hallowell roof plumbing"
Nice to have
• Stick with Logo Colours

```html
<!DOCTYPE html>
<html lang="en">
<head>
<meta charset="utf-8">
<title>hallowell roof plumbing – business card</title>
<link href="https://fonts.googleapis.com/css2?family=Lato:ital,wght@0,400;0,700;1,400&display=swap" rel="stylesheet">
<style>
  :root {
    --backdrop: #4b4b4d;
    --card: #1d1d1f;
    --brand-blue: #2aa6d6;
    --muted: #a9abae;
    --silver: #b9babc;
  }
  * { margin: 0; padding: 0; box-sizing: border-box; }
  html, body {
    width: 1200px; height: 1200px; overflow: hidden;
    background: var(--backdrop);
    font-family: "Lato", Arial, sans-serif;
  }
  .card {
    position: absolute; left: 182px; width: 836px; height: 477px;
    background: var(--card);
  }
  .card--front { top: 94px; }
  .card--back { top: 629px; }

  .brand-name {
    position: absolute; left: 0; right: 0; text-align: center;
    font-weight: 400; text-transform: lowercase; white-space: nowrap;
  }
  .card--front .brand-name {
    top: 150px; font-size: 44px; color: var(--brand-blue); letter-spacing: 1px;
  }
  .card--back .brand-name {
    top: 200px; font-size: 62px; color: var(--silver); letter-spacing: 2px;
  }

  .holder-name {
    position: absolute; left: 30px; top: 298px;
    font-size: 25px; font-weight: 700; color: var(--brand-blue);
  }
  .holder-role {
    position: absolute; left: 31px; top: 330px;
    font-size: 19px; font-style: italic; color: var(--muted);
  }
  .divider {
    position: absolute; left: 112px; right: 0; top: 342px; height: 4px;
    background: var(--brand-blue);
  }
  .services {
    position: absolute; left: 34px; top: 379px; list-style: none;
    font-size: 19px; line-height: 24px; color: var(--brand-blue);
  }
  .services li::before {
    content: ""; display: inline-block; width: 6px; height: 6px;
    background: var(--muted); margin-right: 12px; vertical-align: middle;
  }
  .contact {
    position: absolute; right: 36px; top: 397px; text-align: right;
    font-size: 19px; line-height: 25px; color: var(--muted);
  }
  .contact-line { display: flex; justify-content: flex-end; align-items: center; gap: 12px; }
  .contact-line svg { width: 22px; height: 22px; flex: none; }
</style>
</head>
<body>
  <section class="card card--front" aria-label="Card front">
    <div class="brand-name">hallowell roof plumbing</div>

    <h1 class="holder-name">Owen Hallowell</h1>
    <p class="holder-role">Owner</p>
    <div class="divider"></div>

    <ul class="services">
      <li>Residential &amp; Commercial</li>
      <li>Re-roof &amp; New Construction</li>
      <li>Fully Insured</li>
    </ul>

    <div class="contact">
      <div class="contact-line">
        <span>0417 382 965</span>
        <svg viewBox="0 0 22 22" aria-hidden="true">
          <rect x="6" y="3" width="10" height="17" rx="1.5" fill="none" stroke="#2aa6d6" stroke-width="1.8"/>
          <rect x="8" y="6" width="6" height="4" fill="#2aa6d6"/>
          <line x1="13" y1="3" x2="13" y2="0" stroke="#2aa6d6" stroke-width="1.8"/>
          <g fill="#2aa6d6"><rect x="8" y="12" width="2" height="1.6"/><rect x="12" y="12" width="2" height="1.6"/><rect x="8" y="15" width="2" height="1.6"/><rect x="12" y="15" width="2" height="1.6"/></g>
        </svg>
      </div>
      <div class="contact-line">
        <span>owenhallowellroofing@maildrop-example.com</span>
        <svg viewBox="0 0 22 22" aria-hidden="true">
          <rect x="1" y="5" width="20" height="13" fill="#2aa6d6"/>
          <polyline points="1,5 11,13 21,5" fill="none" stroke="#1d1d1f" stroke-width="1.5"/>
          <polyline points="1,18 8,11 M21,18 14,11" fill="none" stroke="#1d1d1f" stroke-width="1.2"/>
        </svg>
      </div>
    </div>
  </section>

  <section class="card card--back" aria-label="Card back">
    <div class="brand-name">hallowell roof plumbing</div>
  </section>
</body>
</html>
```